Bravo Mend Co - Maintenance Flyer for Exisiting Client base

Design a Flyer for existing clients using a different service (Home Cleaning, KSL Cleaning) to introduce and attract same client to use Home Maintenance Services (Bravo Mend Co).

Home Maintenance is AC, Plumbing, Electrical and Handyman services.

The flyer must have a call to action

Utilize our phone number 800 Gleamo

KSL = The Kind Steady Line

Focus on Quality and Servicing Clients needs 24 Hours a day - 365 days a year.

Associate KSL Cleaning + Bravo Mend Co - so clients understand part of the same family of companies.

Talk about no cost (complimentary) estimates
Speed
Agility
Client First perspective
Same Tech to visit your home each time

Target Market(s)

Home Owners, Apartment Renters

Industry/Entity Type

Property Maintenance

Colors

Designer to choose colors to be used in the design.

Requirements
Must have
• Crisp, Clean and bright design -
• Must be double sided - A5
• Associate KSL Cleaning + Bravo Mend Co - so clients understand part of the same family of companies.
• Introducing Bravo Mend Co, maintenance arm of The Kind Steady Line Cleaning. Just like our cleaning service, we prioritize customer service and getting the job done properly on the first visit.
• Would like to see this on the Flier as well?
• That means no more waiting around for someone unqualified and ill-equipped.
• Bravo Mend Co is reinventing the maintenance industry in Dubai with GPS technology and world class inventory management.
• This means you get the right technician, with the right tools at the right time!
Nice to have
• Talk about no cost (complimentary) estimates
• Speed
• Agility
• Client First perspective
• Same Tech to visit your home each time
Should not have
• Anything animated or silly - must be clean and professional.

```html
<!DOCTYPE html>
<html lang="en">
<head>
<meta charset="utf-8">
<title>Bravo Mend Co – Maintenance Flyer</title>
<link href="https://fonts.googleapis.com/css2?family=Montserrat:wght@400;500;700;800&family=Raleway:wght@400;500;600&display=swap" rel="stylesheet">
<style>
  :root{
    --bg:#d9d9d9;
    --paper:#ffffff;
    --blue:#1f9ae0;
    --deep-blue:#1869b5;
    --red:#b3232d;
    --ink:#2b2b2b;
    --muted:#6d6d6d;
    --grey-1:#e4e4e4;
    --grey-2:#a8a8a8;
    --grey-3:#5f5f5f;
  }
  *{box-sizing:border-box;margin:0;padding:0}
  html,body{width:714px;height:1200px;overflow:hidden;background:var(--bg)}
  body{position:relative;font-family:"Raleway",sans-serif;color:var(--ink)}
  .flyer{position:absolute;left:148px;width:418px;height:588px;background:var(--paper);overflow:hidden;box-shadow:0 2px 8px rgba(0,0,0,.12)}
  .flyer--front{top:8px}
  .flyer--back{top:604px}
  .abs{position:absolute}
  .tile{position:absolute;width:40px;height:40px}
  .tile--red{background:var(--red)}
  .tile--blue{background:var(--deep-blue)}
  .tile--light{background:var(--grey-1)}
  .tile--mid{background:var(--grey-2)}
  .tile--dark{background:var(--grey-3)}
  .tile--outline{border:1px solid var(--grey-1);background:var(--paper)}
  .brand{position:absolute;display:flex;align-items:center;gap:5px;font-family:"Montserrat",sans-serif;font-weight:700;color:var(--deep-blue);white-space:nowrap}
  .brand__dot{width:9px;height:9px;border-radius:50%;background:var(--red)}
  .brand-box{position:absolute;background:var(--paper);border:1px solid var(--grey-1);display:flex;align-items:center;justify-content:center;text-align:center;font-family:"Montserrat",sans-serif;font-weight:700;font-size:9px;line-height:1.1;color:var(--deep-blue)}
  .photo{position:absolute;border:3px solid var(--blue)}
  .photo--tools{background:linear-gradient(135deg,#6b6f78,#c9a64a 55%,#8b8f96)}
  .photo--tech{border:2px solid var(--grey-1);background:linear-gradient(160deg,#dfe3e8,#3d5a8c)}
  .photo--ac{background:linear-gradient(150deg,#eef1f4 30%,#f08a24 60%,#2e4a80)}
  .photo--meter{border:2px solid var(--grey-1);background:linear-gradient(135deg,#3b3f46,#d8b640 50%,#a33)}
  .headline{left:26px;top:232px;font-family:"Montserrat",sans-serif;line-height:1.12}
  .headline__line{font-size:19px;font-weight:400}
  .headline__love{color:var(--red);font-weight:800}
  .headline__brand{font-size:23px;font-weight:800;color:var(--blue)}
  .headline__sub{font-size:9.5px;font-weight:700;margin-top:4px}
  .intro{left:26px;top:340px;width:190px;font-family:"Montserrat",sans-serif;line-height:1.15}
  .intro__hello{color:var(--blue);font-size:13px}
  .intro__name{font-size:15px;font-weight:800}
  .intro__brand{font-size:15px;font-weight:800;color:var(--blue)}
  .intro__text{font-family:"Raleway",sans-serif;font-size:8px;line-height:1.45;color:var(--muted);margin-top:6px}
  .contacts{left:26px;top:480px;display:flex;flex-direction:column;gap:7px}
  .contact{display:flex;align-items:center;gap:8px}
  .contact svg{width:14px;height:14px;flex:none}
  .contact__label{font-size:7px;color:var(--blue);font-weight:600}
  .contact__value{font-size:8.5px;font-weight:600;color:var(--ink)}
  .promise{left:228px;top:236px;display:flex;align-items:center;gap:8px;font-family:"Montserrat",sans-serif}
  .promise__badge{width:38px;height:38px;border:2px solid var(--blue);border-radius:50%;display:flex;align-items:center;justify-content:center;font-size:11px;font-weight:700;color:var(--blue)}
  .promise__text{font-size:11px;line-height:1.2}
  .promise__text b{color:var(--deep-blue)}
  .promise__big{color:var(--red);font-weight:800;font-size:16px}
  .service-title{left:228px;top:286px;font-family:"Montserrat",sans-serif;font-size:12px}
  .service-title b{font-weight:800}
  .features{left:228px;top:312px;width:170px;display:flex;flex-direction:column;gap:16px}
  .feature{display:flex;gap:9px;align-items:flex-start}
  .feature svg{width:24px;height:24px;flex:none}
  .feature__title{font-family:"Montserrat",sans-serif;font-size:9px;font-weight:700;color:var(--ink)}
  .feature__title--blue{color:var(--blue)}
  .feature__text{font-size:7.5px;line-height:1.4;color:var(--muted)}
  .section-head{left:196px;top:328px;font-family:"Montserrat",sans-serif;line-height:1.1;text-align:right;width:196px}
  .section-head__kicker{color:var(--red);font-size:12px}
  .section-head__title{font-size:16px;font-weight:800}
  .section-head__title span{color:var(--deep-blue)}
  .services{left:24px;top:378px;width:370px;display:flex;justify-content:space-between}
  .service{width:86px;display:flex;flex-direction:column;align-items:center;gap:6px;text-align:center}
  .service__tile{width:42px;height:42px;display:flex;align-items:center;justify-content:center}
  .service__tile svg{width:24px;height:24px}
  .service__tile--outline{border:1.5px solid var(--deep-blue);background:var(--paper)}
  .service__tile--blue{background:var(--deep-blue)}
  .service__tile--red{background:var(--red)}
  .service__name{font-size:8.5px;line-height:1.2;color:var(--ink)}
  .cta{left:0;top:458px;width:418px;text-align:center;font-family:"Montserrat",sans-serif;line-height:1.15}
  .cta__web{font-size:8.5px;letter-spacing:2.5px;color:var(--ink)}
  .cta__call{font-size:16px;color:var(--blue)}
  .cta__phone{font-size:27px;font-weight:800}
  .cta__phone span{color:var(--red)}
  .rule{position:absolute;height:1.5px;background:var(--deep-blue)}
  .contact-row{left:24px;top:548px;width:370px;display:flex;justify-content:space-between}
</style>
</head>
<body>

<!-- FRONT -->
<section class="flyer flyer--front">
  <div class="tile tile--red" style="left:160px;top:22px;width:36px;height:28px"></div>
  <div class="tile tile--blue" style="left:70px;top:56px;width:86px;height:40px"></div>
  <div class="tile tile--light" style="left:160px;top:56px;width:36px;height:36px"></div>
  <div class="tile tile--outline" style="left:160px;top:22px;width:0;height:0"></div>
  <div class="tile tile--mid" style="left:18px;top:100px;width:34px;height:30px"></div>
  <div class="tile tile--light" style="left:56px;top:100px;width:36px;height:36px"></div>
  <div class="tile tile--dark" style="left:96px;top:100px;width:36px;height:36px"></div>
  <div class="tile tile--dark" style="left:18px;top:134px;width:34px;height:28px"></div>
  <div class="tile tile--red" style="left:56px;top:140px;width:76px;height:64px"></div>
  <div class="brand-box" style="left:136px;top:100px;width:58px;height:58px">Bravo<br>Mend Co</div>
  <div class="photo photo--tech" style="left:136px;top:162px;width:58px;height:58px" role="img" aria-label="Photo of a technician working on a ceiling fixture"></div>
  <div class="photo photo--tools" style="left:206px;top:60px;width:190px;height:122px" role="img" aria-label="Photo of a tool belt with hammer and pliers"></div>
  <div class="brand" style="left:276px;top:22px;font-size:12px"><span class="brand__dot"></span>KSL Cleaning</div>

  <div class="abs headline">
    <div class="headline__line">We <span class="headline__love">Love</span> To Be</div>
    <div class="headline__line">The Kind Steady Line</div>
    <div class="headline__brand">Bravo Mend Co</div>
    <div class="headline__sub">Same Tech to visit your home<br>Each time</div>
  </div>

  <div class="abs intro">
    <div class="intro__hello">Hello.. We are</div>
    <div class="intro__name">KSL Cleaning &amp;</div>
    <div class="intro__brand">Bravo Mend Co</div>
    <p class="intro__text">Introducing Bravo Mend Co, the maintenance arm of The Kind Steady Line Cleaning. Just like our cleaning service, we put you first and get the job done properly on the first visit, with the right tech and tools.</p>
  </div>

  <div class="abs contacts">
    <div class="contact">
      <svg viewBox="0 0 24 24"><path d="M5 4h4l2 5-2.5 1.5a11 11 0 0 0 5 5L15 13l5 2v4a2 2 0 0 1-2 2A16 16 0 0 1 3 6a2 2 0 0 1 2-2z" fill="none" stroke="#999" stroke-width="1.8"/></svg>
      <div><div class="contact__label">Tel Number</div><div class="contact__value">800</div></div>
    </div>
    <div class="contact">
      <svg viewBox="0 0 24 24"><rect x="3" y="6" width="18" height="12" fill="none" stroke="#999" stroke-width="1.8"/><path d="M3 6l9 7 9-7" fill="none" stroke="#999" stroke-width="1.8"/></svg>
      <div><div class="contact__label">Support Service</div><div class="contact__value">support@kslcleaning.com</div></div>
    </div>
    <div class="contact">
      <svg viewBox="0 0 24 24"><path d="M12 22s7-7 7-12a7 7 0 0 0-14 0c0 5 7 12 7 12z" fill="#999"/><circle cx="12" cy="10" r="2.5" fill="#fff"/></svg>
      <div><div class="contact__label">Address</div><div class="contact__value">Your Address Goes Here</div></div>
    </div>
  </div>

  <div class="abs promise">
    <div class="promise__badge">24/7</div>
    <div class="promise__text">Servicing <b>Clients</b><br><span class="promise__big">365</span> Days a Year.</div>
  </div>
  <div class="abs service-title">The <b>Perfect</b> Service</div>

  <div class="abs features">
    <div class="feature">
      <svg viewBox="0 0 24 24"><path d="M3 17a9 9 0 0 1 18 0" fill="none" stroke="#222" stroke-width="2.4"/><path d="M12 17l5-6" stroke="#222" stroke-width="2"/><circle cx="12" cy="17" r="2" fill="#222"/></svg>
      <div><div class="feature__title feature__title--blue">SPEED</div><div class="feature__text">The right technician, with the right tools, on time.</div></div>
    </div>
    <div class="feature">
      <svg viewBox="0 0 24 24"><circle cx="12" cy="10" r="7" fill="#b3232d"/><path d="M8 16l-2 6 6-3 6 3-2-6" fill="#b3232d"/><path d="M9 10l2 2 4-4" fill="none" stroke="#fff" stroke-width="1.8"/></svg>
      <div><div class="feature__title">AGILITY</div><div class="feature__text">GPS routing and smart inventory for every job.</div></div>
    </div>
    <div class="feature">
      <svg viewBox="0 0 24 24"><circle cx="12" cy="9" r="5" fill="#222"/><path d="M3 22a9 7 0 0 1 18 0z" fill="#222"/></svg>
      <div><div class="feature__title feature__title--blue">CLIENT FIRST</div><div class="feature__text">Complimentary estimates and the same tech each visit.</div></div>
    </div>
  </div>
</section>

<!-- BACK -->
<section class="flyer flyer--back">
  <div class="tile tile--mid" style="left:330px;top:14px;width:36px;height:30px"></div>
  <div class="tile tile--blue" style="left:240px;top:34px;width:86px;height:40px"></div>
  <div class="tile tile--light" style="left:330px;top:48px;width:36px;height:30px"></div>
  <div class="tile tile--dark" style="left:370px;top:48px;width:34px;height:30px"></div>
  <div class="tile tile--red" style="left:330px;top:82px;width:74px;height:50px"></div>
  <div class="tile tile--red" style="left:160px;top:78px;width:40px;height:26px"></div>
  <div class="tile tile--light" style="left:204px;top:78px;width:40px;height:32px"></div>
  <div class="tile tile--outline" style="left:204px;top:114px;width:40px;height:36px"></div>
  <div class="brand-box" style="left:250px;top:78px;width:70px;height:64px">Bravo<br>Mend Co</div>
  <div class="photo photo--meter" style="left:330px;top:136px;width:74px;height:56px" role="img" aria-label="Photo of hands testing wiring with a multimeter"></div>
  <div class="brand" style="left:24px;top:136px;font-size:12px"><span class="brand__dot"></span>KSL Cleaning</div>
  <div class="photo photo--ac" style="left:24px;top:158px;width:190px;height:150px" role="img" aria-label="Photo of a technician in a hard hat servicing a wall air conditioner"></div>

  <div class="abs section-head">
    <div class="section-head__kicker">Learn More</div>
    <div class="section-head__title">About Our <span>Services</span></div>
  </div>

  <div class="abs services">
    <div class="service">
      <div class="service__tile service__tile--outline"><svg viewBox="0 0 24 24"><path d="M5 19l9-9M14 10l3-3 2 2-3 3" stroke="#b3232d" stroke-width="2.4" fill="none"/><path d="M6 5l13 13" stroke="#1869b5" stroke-width="2.4"/></svg></div>
      <div class="service__name">Home<br>Maintenance</div>
    </div>
    <div class="service">
      <div class="service__tile service__tile--blue"><svg viewBox="0 0 24 24"><path d="M6 4v8h10v8" fill="none" stroke="#f2c230" stroke-width="3"/><path d="M13 20h6" stroke="#f2c230" stroke-width="3"/></svg></div>
      <div class="service__name">Plumbing</div>
    </div>
    <div class="service">
      <div class="service__tile service__tile--outline"><svg viewBox="0 0 24 24"><path d="M4 14h12l4-4v8l-4-4" fill="#b3232d"/><rect x="4" y="10" width="8" height="4" fill="#b3232d"/></svg></div>
      <div class="service__name">Electrical &amp;<br>Handyman Services</div>
    </div>
    <div class="service">
      <div class="service__tile service__tile--red"><svg viewBox="0 0 24 24"><rect x="3" y="8" width="18" height="7" rx="1" fill="#f3efe6"/><path d="M6 13h12" stroke="#e0a33a" stroke-width="1.5"/></svg></div>
      <div class="service__name">Air Conditioning<br>Services</div>
    </div>
  </div>

  <div class="abs cta">
    <div class="cta__web">WWW.KSLCLEANING.COM</div>
    <div class="cta__call">Call Us Now</div>
    <div class="cta__phone"><span>800</span> Gleamo</div>
  </div>

  <div class="rule" style="left:24px;top:538px;width:140px"></div>
  <div class="rule" style="left:254px;top:538px;width:140px"></div>

  <div class="abs contact-row">
    <div class="contact">
      <svg viewBox="0 0 24 24"><path d="M5 4h4l2 5-2.5 1.5a11 11 0 0 0 5 5L15 13l5 2v4a2 2 0 0 1-2 2A16 16 0 0 1 3 6a2 2 0 0 1 2-2z" fill="none" stroke="#999" stroke-width="1.8"/></svg>
      <div><div class="contact__label">Tel Number</div><div class="contact__value">800</div></div>
    </div>
    <div class="contact">
      <svg viewBox="0 0 24 24"><rect x="3" y="6" width="18" height="12" fill="none" stroke="#999" stroke-width="1.8"/><path d="M3 6l9 7 9-7" fill="none" stroke="#999" stroke-width="1.8"/></svg>
      <div><div class="contact__label">Support Service</div><div class="contact__value">support@kslcleaning.com</div></div>
    </div>
    <div class="contact">
      <svg viewBox="0 0 24 24"><path d="M12 22s7-7 7-12a7 7 0 0 0-14 0c0 5 7 12 7 12z" fill="#999"/><circle cx="12" cy="10" r="2.5" fill="#fff"/></svg>
      <div><div class="contact__label">Address</div><div class="contact__value">Your Address Goes Here</div></div>
    </div>
  </div>
</section>

</body>
</html>
```